Meadowlyn Acres Website Design

We have been redeveloping our website already and are quite happy with the content, but the design needs to be better:
https://harvo-link.example-host.com/

Pages, content, concept etc. Can all be taken from the redeveloped website.
The farmer can register and edit/view their profile, subscribe and these pages need to be designed better as well as contact, about, pricing, tos, privacy and a page with example portlets.

We need a website to appeal to farmers, investors and retiring farmers.

The design should be clean and a little country.

We don't want any repeat designs that some may submit to every project and has no respect for the project brief, so please don't submit them.

Target Market(s)

farmers, investors, retirees

Industry/Entity Type

Farming

Number of Pages Required

5+ page

Colors

Designer to choose colors to be used in the design.

Requirements
Must have
• Nice, clean modern design that is appealing
• Profile page laid out nicely

```html
<!DOCTYPE html>
<html lang="en">
<head>
<meta charset="utf-8">
<title>Meadowlyn Acres – Login</title>
<link href="https://fonts.googleapis.com/css2?family=Questrial&family=Roboto:wght@400;500;700&display=swap" rel="stylesheet">
<style>
:root{
  --green:#3aaa3f;
  --green-dark:#2e8f33;
  --orange:#fb8405;
  --ink:#222;
  --muted:#444;
  --field:#e6e6e6;
  --field-icon:#9d9d9d;
  --footer:#3b3b3b;
  --footer-line:#4c4c4c;
  --footer-text:#b4b4b4;
  --red:#d33a2c;
  --blue:#3a5a99;
}
*{box-sizing:border-box;margin:0;padding:0}
html,body{width:910px;height:1200px;overflow:hidden}
body{position:relative;font-family:'Roboto',sans-serif;color:var(--ink);background:#fff}
.site-header{position:absolute;left:0;top:0;width:910px;height:70px;background:#f5f5f3;z-index:3}
.brand-badge{position:absolute;left:58px;top:0;width:88px;height:93px;background:#fff;border-radius:0 0 44px 44px;display:flex;align-items:center;justify-content:center;text-align:center;font-family:'Questrial',sans-serif;font-size:13px;line-height:1.15;color:var(--green-dark);padding-top:6px}
.main-nav{position:absolute;left:171px;top:29px;display:flex;gap:17px;font-size:11px;font-weight:500;color:#333;letter-spacing:.1px}
.main-nav a{color:inherit;text-decoration:none;padding-bottom:4px}
.main-nav a.active{color:var(--green);border-bottom:2px solid var(--green)}
.account-link{position:absolute;left:718px;top:29px;font-size:11px;font-weight:500;color:var(--orange);display:flex;align-items:center;gap:6px}
.hero{position:absolute;left:0;top:70px;width:910px;height:195px;background:linear-gradient(90deg,#3b4a2c 0%,#58683e 30%,#44523a 55%,#6d7e4a 80%,#8a9a5a 100%)}
.hero-title{position:absolute;left:0;top:79px;width:910px;text-align:center;font-family:'Questrial',sans-serif;font-size:35px;color:#fff}
.breadcrumb{position:absolute;left:0;top:265px;width:910px;height:30px;background:#f3f3f3;font-size:13px;padding:9px 0 0 55px;color:#333}
.breadcrumb a{color:var(--green);text-decoration:none}
.landscape{position:absolute;left:0;top:295px;width:910px;height:648px;background:linear-gradient(180deg,#c9cbc4 0%,#a7a89a 28%,#4f5a3a 52%,#5e6a33 70%,#7b7a3a 85%,#4b4a26 100%)}
.auth-frame{position:absolute;left:262px;top:338px;width:387px;height:562px;background:var(--green);border-radius:3px}
.panel{position:absolute;left:6px;width:375px;background:#fff;border-radius:3px}
.panel-login{top:6px;height:437px}
.panel-join{top:451px;height:104px}
.panel h2{font-family:'Questrial',sans-serif;font-weight:400;text-align:center;color:var(--ink)}
.panel-title{position:absolute;left:0;width:100%;font-size:20px}
.lede{position:absolute;left:0;top:52px;width:100%;text-align:center;font-size:11px;color:#333}
.field{position:absolute;left:14px;width:346px;height:36px;background:var(--field);border-radius:2px;font-size:13px;color:#555;padding:10px 0 0 14px}
.field .tag{position:absolute;right:0;top:0;width:35px;height:36px;border-radius:0 2px 2px 0;display:flex;align-items:center;justify-content:center}
.tag.red{background:var(--red)}
.tag.blue{background:var(--blue)}
.tag.grey{background:var(--field-icon)}
.divider{position:absolute;left:0;top:194px;width:100%;border-top:1px solid #e4e4e4}
.or-badge{position:absolute;left:168px;top:174px;width:39px;height:39px;border-radius:50%;background:#e6e6e6;font-weight:700;font-size:14px;display:flex;align-items:center;justify-content:center;color:#333}
.btn{position:absolute;left:14px;width:346px;height:33px;background:var(--orange);color:#fff;border-radius:3px;font-weight:700;font-size:15px;display:flex;align-items:center;justify-content:center}
.forgot{position:absolute;left:0;top:405px;width:100%;text-align:center;font-size:10.5px;color:var(--green-dark)}
.site-footer{position:absolute;left:0;top:943px;width:910px;height:257px;background:var(--footer);color:#fff}
.col-rule{position:absolute;top:28px;height:150px;border-left:1px solid var(--footer-line)}
.footer-heading{position:absolute;font-size:12.5px;font-weight:500}
.post{position:absolute;left:56px;width:260px}
.post-date{position:absolute;left:0;top:0;width:47px;height:47px;background:var(--green);text-align:center;color:#fff}
.post-date b{display:block;font-size:22px;font-weight:700;line-height:1;padding-top:6px}
.post-date span{font-size:9px}
.post-title{position:absolute;left:60px;top:0;width:200px;font-size:12.5px;font-weight:500;line-height:1.35}
.post-by{position:absolute;left:60px;top:41px;font-size:11px;color:var(--footer-text);white-space:nowrap}
.news-copy{position:absolute;left:377px;top:56px;width:250px;font-size:11px;line-height:1.55;color:var(--footer-text)}
.news-input{position:absolute;left:377px;top:98px;width:251px;height:27px;background:#fff;border-radius:14px;font-size:11px;color:#888;padding:7px 0 0 13px}
.news-btn{position:absolute;left:377px;top:133px;width:97px;height:27px;background:var(--orange);border-radius:14px;font-size:12.5px;font-weight:500;display:flex;align-items:center;justify-content:center}
.footer-brand{position:absolute;left:657px;top:120px;width:212px;text-align:center;font-family:'Questrial',sans-serif;font-size:20px;color:#b9b9b9}
.footer-mark{position:absolute;left:739px;top:30px;width:48px;height:48px;border:1px solid #8a8a8a;border-radius:50%}
.footer-base{position:absolute;left:0;top:209px;width:910px;border-top:1px solid var(--footer-line)}
.legal{position:absolute;left:55px;top:227px;font-size:11px;color:var(--footer-text)}
.social{position:absolute;left:773px;top:222px;display:flex;gap:6px}
.social span{width:23px;height:23px;border-radius:50%;background:#8e8e8e;display:block}
</style>
</head>
<body>
<header class="site-header">
  <div class="brand-badge">Meadowlyn<br>Acres</div>
  <nav class="main-nav">
    <a class="active">HOME</a><a>ASPIRING FARMERS</a><a>INVESTORS</a><a>RETIRING FARMER</a><a>BLOG</a><a>PRICING</a><a>CONTACT</a>
  </nav>
  <div class="account-link">
    <svg width="11" height="11" viewBox="0 0 11 11" fill="none" stroke="#fb8405" stroke-width="1.2"><path d="M4 1h6v9H4M1 5.5h6M5 3.5l2 2-2 2"/></svg>
    SIGN IN OR SIGN UP
  </div>
</header>

<section class="hero" role="img" aria-label="Photo of a smiling farming family with young children outdoors among trees">
  <h1 class="hero-title">Login</h1>
</section>

<div class="breadcrumb"><a>Home</a> / Login</div>

<main class="landscape" role="img" aria-label="Photo of a sunlit pasture with grazing cattle, hills and a rider on horseback">
</main>

<div class="auth-frame">
  <section class="panel panel-login">
    <h2 class="panel-title" style="top:22px">Social Login</h2>
    <p class="lede">It only takes a couple of seconds!</p>
    <div class="field" style="top:71px">Northpass<span class="tag red"></span></div>
    <div class="field" style="top:117px">Fernbook<span class="tag blue"></span></div>
    <div class="divider"></div>
    <div class="or-badge">or</div>
    <h2 class="panel-title" style="top:231px">Login</h2>
    <div class="field" style="top:264px">Email*
      <span class="tag grey"><svg width="20" height="14" viewBox="0 0 20 14" fill="none" stroke="#fff" stroke-width="1.2"><rect x="1" y="1" width="18" height="12"/><path d="M1 1l9 7 9-7M1 13l6-6M19 13l-6-6"/></svg></span>
    </div>
    <div class="field" style="top:310px">Password*
      <span class="tag grey"><svg width="14" height="20" viewBox="0 0 14 20" fill="none" stroke="#fff" stroke-width="1.2"><path d="M3 8V5a4 4 0 0 1 8 0v3"/><rect x="1" y="8" width="12" height="11" rx="3"/><path d="M7 12v3"/></svg></span>
    </div>
    <div class="btn" style="top:360px">LOGIN</div>
    <p class="forgot">Forgot Your Password?</p>
  </section>
  <section class="panel panel-join">
    <h2 class="panel-title" style="top:20px">Don't have an Account?</h2>
    <div class="btn" style="top:55px">JOIN US</div>
  </section>
</div>

<footer class="site-footer">
  <div class="col-rule" style="left:343px"></div>
  <div class="col-rule" style="left:657px"></div>
  <h3 class="footer-heading" style="left:54px;top:26px">From The Blog</h3>
  <article class="post" style="top:58px">
    <div class="post-date"><b>24</b><span>APR 17</span></div>
    <h4 class="post-title">Out of the Griddle Hollow into the fire of soil health | Tom Reddan</h4>
    <p class="post-by">Posted by Tom Reddan</p>
  </article>
  <article class="post" style="top:134px">
    <div class="post-date"><b>21</b><span>APR 17</span></div>
    <h4 class="post-title">Harvey is a cool name, so is Elsie, but their passion for farming</h4>
    <p class="post-by">Posted by Harvey and Elsie</p>
  </article>
  <h3 class="footer-heading" style="left:376px;top:26px">Subscribe To Our Newsletter</h3>
  <p class="news-copy">Want to be the first to know about our amazing discount offer?</p>
  <div class="news-input">Email Address</div>
  <div class="news-btn">Subscribe</div>
  <div class="footer-mark"></div>
  <div class="footer-brand">Meadowlyn Acres</div>
  <div class="footer-base"></div>
  <p class="legal">©2017 Meadowlyn Acres. Terms of Use | Privay | Sitemap | Donate</p>
  <div class="social"><span></span><span></span><span></span></div>
</footer>
</body>
</html>
```